ROVA Pty Ltd Business Card

Looking for a simple yet eye-catching double-sided business card design using my company logo on one side and contact details on the other.

Target Market(s)

Government

Industry/Entity Type

Communication Systems Engineering

Contact Information for Business Card

ROVA Pty Ltd

Requirements
Nice to have
• Would be great to have a QR code so details can be scanned into contacts

```html
<!DOCTYPE html>
<html lang="en">
<head>
<meta charset="utf-8">
<title>ROVA Pty Ltd Business Card</title>
<link href="https://fonts.googleapis.com/css2?family=Montserrat:wght@400;500;700&display=swap" rel="stylesheet">
<style>
  :root {
    --page: #1d2125;
    --card: #333d45;
    --ink: #ffffff;
    --ink-soft: #d5d9dc;
    --tab: #e6e7e8;
    --trace: #8d959b;
  }
  * { margin: 0; padding: 0; box-sizing: border-box; }
  html, body { width: 1200px; height: 952px; overflow: hidden; }
  body {
    background: var(--page);
    font-family: "Montserrat", sans-serif;
    display: flex;
    align-items: center;
    justify-content: center;
    gap: 60px;
  }
  .card {
    position: relative;
    width: 520px;
    height: 300px;
    background: var(--card);
    border-radius: 22px;
    overflow: hidden;
    box-shadow: 0 18px 40px rgba(0,0,0,0.45);
  }
  /* Front */
  .tab {
    position: absolute;
    width: 96px;
    height: 34px;
    background: var(--tab);
    border-radius: 8px;
  }
  .tab--top { top: 0; left: 0; border-radius: 0 0 8px 0; }
  .tab--bottom { bottom: 0; right: 0; border-radius: 8px 0 0 0; }
  .brand {
    display: flex;
    align-items: center;
    gap: 14px;
    color: var(--ink);
    font-weight: 700;
    letter-spacing: 0.04em;
  }
  .brand__dot {
    width: 18px; height: 18px;
    border-radius: 50%;
    background: var(--ink);
  }
  .front .brand {
    position: absolute;
    inset: 0;
    justify-content: center;
    font-size: 64px;
  }
  .front .brand__dot { width: 26px; height: 26px; }
  /* Back */
  .back .brand {
    position: absolute;
    top: 30px; left: 34px;
    font-size: 40px;
  }
  .contact {
    position: absolute;
    top: 100px; left: 34px;
    list-style: none;
    color: var(--ink-soft);
    font-size: 12px;
    line-height: 1.45;
  }
  .contact li { display: flex; gap: 10px; margin-bottom: 7px; }
  .contact svg { width: 11px; height: 11px; flex: none; margin-top: 3px; fill: var(--ink-soft); }
  .person {
    position: absolute;
    top: 34px; right: 34px;
    text-align: right;
    color: var(--ink);
  }
  .person__name { font-size: 18px; font-weight: 400; letter-spacing: 0.03em; }
  .person__name strong { font-weight: 700; }
  .person__role {
    display: inline-block;
    margin-top: 4px;
    padding-bottom: 6px;
    font-size: 13px;
    color: var(--ink-soft);
    border-bottom: 1.5px solid var(--ink-soft);
  }
  .circuit-art {
    position: absolute;
    right: 0; bottom: 0;
    width: 300px; height: 170px;
    border-top-left-radius: 60px;
    background: radial-gradient(ellipse at 60% 70%, rgba(141,149,155,0.35), rgba(141,149,155,0) 70%);
  }
</style>
</head>
<body>
  <section class="card front">
    <div class="tab tab--top"></div>
    <div class="tab tab--bottom"></div>
    <div class="brand"><span class="brand__dot"></span>ROVA</div>
  </section>

  <section class="card back">
    <div class="brand"><span class="brand__dot"></span>ROVA</div>
    <ul class="contact">
      <li><svg viewBox="0 0 10 10"><path d="M5 0a3.5 3.5 0 0 0-3.5 3.5C1.5 6 5 10 5 10s3.5-4 3.5-6.5A3.5 3.5 0 0 0 5 0zm0 5a1.4 1.4 0 1 1 0-2.8A1.4 1.4 0 0 1 5 5z"/></svg><span>14-16 Harbour Lane Redfern<br>NSW 2016 Australia</span></li>
      <li><svg viewBox="0 0 10 10"><path d="M2 0l2 2.5-1.2 1.4a6 6 0 0 0 3.3 3.3L7.5 6 10 8l-1.5 2C4 10 0 6 0 1.5z"/></svg><span>+00 987 654 32</span></li>
      <li><svg viewBox="0 0 10 10"><path d="M0 1.5h10v7H0zM0.8 2.3L5 5.6l4.2-3.3"/></svg><span>admin@rova.com.au</span></li>
      <li><svg viewBox="0 0 10 10"><path d="M5 0l4 9-4-2-4 2z"/></svg><span>www.rova.com.au</span></li>
    </ul>
    <div class="person">
      <div class="person__name">DANIEL J. <strong>HARWOOD</strong></div>
      <div class="person__role">Managing Director</div>
    </div>
    <div class="circuit-art" role="img" aria-label="Decorative circuit-board tree pattern in light grey lines"></div>
  </section>
</body>
</html>
```